Marlo Tidy Yard Website

We need a website design for this new company. I've attached the company logo. This company is in the construction industry that provides general labor, maintenance and cleaning for construction sites. We want a clean and simple website that can be easy to navigate.

Target Market(s)

Construction industry

Industry/Entity Type

Construction

Number of Pages Required

2 page

Font styles to use
Sans Serif

```html
<!DOCTYPE html>
<html lang="en">
<head>
<meta charset="utf-8">
<title>Marlo Tidy Yard</title>
<link href="https://fonts.googleapis.com/css2?family=Lato:wght@400;700;900&family=Roboto:ital,wght@0,400;0,500;0,700;1,400&display=swap" rel="stylesheet">
<style>
:root{
  --orange:#f05a1a;
  --navy:#0d0b5e;
  --ink:#1b1b1b;
  --text:#6b6b6b;
  --light:#f2f2f2;
  --white:#ffffff;
}
*{box-sizing:border-box;margin:0;padding:0}
html,body{width:1200px;height:3947px;overflow:hidden}
body{position:relative;background:var(--white);font-family:'Roboto',sans-serif;color:var(--text)}
.abs{position:absolute}
.heading{font-family:'Lato',sans-serif;font-weight:900;color:var(--ink);text-align:center;width:1200px;left:0;white-space:nowrap}
.ghost{font-family:'Lato',sans-serif;font-weight:900;color:rgba(0,0,0,.06);text-align:center;width:1200px;left:0;font-size:78px;letter-spacing:2px;white-space:nowrap}
.lede{font-size:13px;line-height:25px;text-align:center;color:var(--text)}
.btn{background:var(--orange);color:var(--white);font-family:'Roboto',sans-serif;font-weight:700;font-size:14px;display:flex;align-items:center;justify-content:center;gap:8px;text-transform:uppercase;white-space:nowrap}
.btn .dot{width:13px;height:13px;border-radius:50%;background:var(--white);display:inline-flex;align-items:center;justify-content:center}

/* header */
.top-rule{left:0;top:0;width:1200px;height:6px;background:var(--orange)}
.brand{left:113px;top:52px;display:flex;align-items:center;gap:12px;font-family:'Lato',sans-serif;font-weight:900;font-size:34px;color:var(--navy);white-space:nowrap}
.brand .mark{width:20px;height:20px;background:var(--orange)}
.contact-line{right:113px;top:44px;font-size:14px;color:var(--text);display:flex;gap:14px;align-items:center;white-space:nowrap}
.contact-line svg{vertical-align:-2px;margin-right:5px}
.nav{right:113px;top:90px;display:flex;gap:31px;font-family:'Roboto',sans-serif;font-weight:700;font-size:15px;color:var(--ink);white-space:nowrap}
.nav .active{color:var(--navy)}

/* hero */
.hero-photo{left:0;top:150px;width:1200px;height:576px;background:linear-gradient(180deg,#9fb0c4 0%,#c8cdd1 40%,#6e5a45 75%,#3e332a 100%)}
.hero-box{left:110px;top:384px;width:490px;height:182px;background:var(--orange);padding:28px 36px}
.hero-box h1{font-family:'Lato',sans-serif;font-weight:900;font-size:45px;color:var(--white);letter-spacing:1px;white-space:nowrap}
.hero-box p{font-weight:700;font-size:16px;line-height:24px;color:var(--white);margin-top:8px}
.slide-arrow{top:418px;width:38px;height:38px;border-radius:50%;background:rgba(60,60,60,.55);display:flex;align-items:center;justify-content:center}

/* services */
.services-bg{left:0;top:726px;width:1200px;height:840px;background:linear-gradient(180deg,#f7f7f7 0%,#ececec 100%)}
.card{top:1034px;width:285px;height:300px;background:var(--white);border:1px solid #dcdcdc;text-align:center;padding-top:32px}
.card.featured{top:1021px;width:320px;height:321px;background:var(--navy);border:none;padding-top:40px;box-shadow:0 6px 18px rgba(0,0,0,.25)}
.card .icon{width:76px;height:76px;margin:0 auto;display:block}
.card h3{font-family:'Lato',sans-serif;font-weight:700;font-size:21px;color:var(--ink);margin-top:20px}
.card.featured h3{color:var(--white)}
.card .bar{width:56px;height:3px;background:var(--orange);margin:12px auto 16px}
.card p{font-size:14px;line-height:24px;color:var(--text);padding:0 38px}
.card.featured p{color:var(--white)}

/* about */
.about-panel{left:0;top:1566px;width:613px;height:424px;background:#ececec}
.about-photo{left:613px;top:1566px;width:587px;height:424px;background:linear-gradient(135deg,#8aa2bd 0%,#3b4f72 45%,#c98a3a 80%,#6b6b6b 100%)}
.about-ghost{left:22px;top:1590px;height:380px;writing-mode:vertical-rl;transform:rotate(180deg);font-family:'Lato',sans-serif;font-weight:900;font-size:72px;line-height:80px;color:rgba(0,0,0,.07);white-space:nowrap;text-align:center}
.about-title{left:110px;top:1632px;font-family:'Lato',sans-serif;font-weight:900;font-size:40px;color:var(--ink);white-space:nowrap}
.about-copy{left:110px;top:1704px;width:443px;font-size:13.5px;line-height:24px;text-align:justify}

/* projects */
.project{top:2261px;height:195px;width:233px}
.dots{left:520px;top:2517px;display:flex;gap:9px}
.dots span{width:30px;height:4px;background:var(--navy)}
.dots span.on{background:var(--orange)}

/* testimonial */
.quote-band{left:0;top:2627px;width:1200px;height:247px;background:var(--orange)}
.quote-text{left:110px;top:2688px;width:740px;font-style:italic;font-size:15.5px;line-height:26px;color:var(--white)}
.quote-name{left:110px;top:2788px;font-family:'Lato',sans-serif;font-weight:900;font-size:18px;color:var(--ink);white-space:nowrap}
.quote-name small{font-family:'Roboto',sans-serif;font-weight:400;font-size:14px;color:var(--white)}
.quote-badge{left:903px;top:2685px;width:132px;height:132px;border-radius:50%;background:var(--navy);display:flex;align-items:center;padding-left:26px}
.quote-photo{left:968px;top:2685px;width:117px;height:117px;border-radius:50%;background:linear-gradient(160deg,#e8e8e8,#a9a9a9);border:4px solid var(--white)}
.band-arrow{top:2735px}

/* blog */
.post{top:3143px;width:472px;height:208px;background:var(--white);box-shadow:0 2px 10px rgba(0,0,0,.14);display:flex}
.post .thumb{width:187px;height:208px;flex:none}
.post .body{padding:26px 24px 0 26px}
.post h4{font-family:'Lato',sans-serif;font-weight:900;font-size:20px;color:var(--ink);white-space:nowrap}
.post .date{font-size:12px;color:var(--ink);margin-top:8px;display:flex;align-items:center;gap:6px}
.post p{font-size:13px;line-height:19px;margin-top:10px;text-align:justify}
.post .meta{display:flex;justify-content:space-between;margin-top:14px;font-size:12px}
.post .more{color:var(--orange);font-weight:700;text-decoration:underline;display:flex;align-items:center;gap:5px}

/* footer */
.foot-building{left:0;top:3566px;width:400px;height:381px;background:linear-gradient(180deg,#b8c8d8 0%,#6f8aa3 55%,#4a5a49 100%)}
.foot-center{left:400px;top:3566px;width:400px;height:381px;background:var(--navy)}
.foot-map{left:800px;top:3566px;width:400px;height:381px;background:linear-gradient(135deg,#eef0ea,#dfe3da)}
.up-btn{left:572px;top:3540px;width:56px;height:56px;border-radius:50%;background:var(--white);display:flex;align-items:center;justify-content:center}
.foot-title{font-family:'Lato',sans-serif;font-weight:700;font-size:14.5px;color:var(--white);width:400px;left:400px;text-align:center}
.email-field{left:455px;top:3677px;width:285px;height:37px;border:1px solid #c7c7e0;color:var(--white);font-size:12px;padding:11px 10px}
.subscribe{left:534px;top:3727px;width:132px;height:37px;font-size:13px}
.foot-line{left:400px;width:400px;display:flex;justify-content:center;align-items:center;gap:12px;font-size:13.5px;color:var(--white);white-space:nowrap}
.direction{left:816px;top:3613px;width:137px;height:32px;background:var(--white);box-shadow:0 1px 4px rgba(0,0,0,.25);font-size:11px;font-weight:500;color:var(--ink);display:flex;align-items:center;justify-content:center;gap:6px;text-transform:uppercase}
</style>
</head>
<body>

<div class="abs top-rule"></div>
<div class="abs brand"><span class="mark"></span>Marlo Tidy Yard</div>
<div class="abs contact-line">
  <span><svg width="12" height="12" viewBox="0 0 24 24"><path fill="#f05a1a" d="M6.6 10.8a15 15 0 0 0 6.6 6.6l2.2-2.2a1 1 0 0 1 1-.25 11.4 11.4 0 0 0 3.6.6 1 1 0 0 1 1 1V20a1 1 0 0 1-1 1A17 17 0 0 1 3 4a1 1 0 0 1 1-1h3.5a1 1 0 0 1 1 1c0 1.25.2 2.45.6 3.6a1 1 0 0 1-.25 1z"/></svg>(+123) 555 010 2040</span>
  <span>|</span>
  <span><svg width="13" height="11" viewBox="0 0 24 18"><path fill="#f05a1a" d="M0 0h24v18H0zM2 2l10 7 10-7z"/></svg>info@marlotidyyard.com</span>
</div>
<nav class="abs nav">
  <span class="active">HOME</span><span>ABOUT US</span><span>INDUSTRY</span><span>SERVICES</span><span>BLOG</span><span>CONTACT US</span>
</nav>

<div class="abs hero-photo" role="img" aria-label="Construction worker on a building site under a crane and blue sky"></div>
<div class="abs hero-box">
  <h1>MARLO TIDY YARD</h1>
  <p>Lorem ipsum dolor sit amet consectetur adipiscing eiusmod tempor incididunt aliqua.</p>
</div>
<div class="abs slide-arrow" style="left:22px"><svg width="12" height="14" viewBox="0 0 12 14"><path d="M9 1 3 7l6 6" stroke="#fff" stroke-width="2.5" fill="none"/></svg></div>
<div class="abs slide-arrow" style="left:1140px"><svg width="12" height="14" viewBox="0 0 12 14"><path d="M3 1l6 6-6 6" stroke="#fff" stroke-width="2.5" fill="none"/></svg></div>

<div class="abs services-bg" role="img" aria-label="Faded construction scaffolding backdrop"></div>
<div class="abs ghost" style="top:805px">WHAT WE DO</div>
<h2 class="abs heading" style="top:825px;font-size:40px">OUR SERVICES</h2>
<p class="abs lede" style="left:250px;width:700px;top:906px">At vero eos et accusamus et iusto odio dignissimos ducimus qui blanditiis praesentium voluptatum deleniti atque corrupti quos dolores et quas molestias excepturi sint occaecati cupiditate non provident, similique sunt in culpa qui officia deserunt mollitia animi, id est laborum et dolorum fuga. Et harum quidem rerum facilis est et expedita distinctio.</p>

<div class="abs card" style="left:155px">
  <svg class="icon" viewBox="0 0 76 76" fill="none" stroke="#f05a1a" stroke-width="2.5" stroke-linejoin="round" stroke-linecap="round">
    <path d="M16 40a22 22 0 0 1 44 0"/><path d="M10 40h56v6H10z"/><path d="M33 19v-4h10v4"/><path d="M38 22v14"/><path d="M14 72c2-12 12-18 24-18s22 6 24 18"/><path d="M38 54v18"/>
  </svg>
  <h3>General Labor</h3><div class="bar"></div>
  <p>I must explain to you mistaken idea of denouncing pleasure and pain was born and I will give you</p>
</div>
<div class="abs card featured" style="left:440px">
  <svg class="icon" viewBox="0 0 76 76" fill="none" stroke="#ffffff" stroke-width="2.5" stroke-linejoin="round" stroke-linecap="round">
    <path d="M34 6h8l1.5 7 5 2 6-4 6 6-4 6 2 5 7 1.5v8l-7 1.5-2 5 4 6-6 6-6-4-5 2L42 70h-8l-1.5-7-5-2-6 4-6-6 4-6-2-5L10 42v-8l7-1.5 2-5-4-6 6-6 6 4 5-2z"/>
    <circle cx="38" cy="38" r="14"/><path d="M31 45l10-10"/><path d="M41 31a4 4 0 1 0 4 4"/>
  </svg>
  <h3>Maintenance</h3><div class="bar"></div>
  <p>I must explain to you mistaken idea of denouncing pleasure and pain was born and I will give you</p>
</div>
<div class="abs card" style="left:760px">
  <svg class="icon" viewBox="0 0 76 76" fill="none" stroke="#f05a1a" stroke-width="2.5" stroke-linejoin="round" stroke-linecap="round">
    <path d="M12 40h24l-3 30H15z"/><path d="M14 40c0-6 4-9 10-9s10 3 10 9"/><path d="M42 30h14v40H42z"/><path d="M45 30v-8h8v8"/><path d="M53 22h10l4-6"/><path d="M63 14l4 2M64 22h5M60 8l2 4"/><path d="M47 44h4M47 52h4"/>
  </svg>
  <h3>Site Cleaning</h3><div class="bar"></div>
  <p>I must explain to you mistaken idea of denouncing pleasure and pain was born and I will give you</p>
</div>
<div class="abs btn" style="left:490px;top:1405px;width:221px;height:50px">See how it works <span class="dot"><svg width="7" height="8" viewBox="0 0 7 8"><path d="M2 1l3 3-3 3" stroke="#f05a1a" stroke-width="1.8" fill="none"/></svg></span></div>

<div class="abs about-panel"></div>
<div class="abs about-ghost">ABOUT US</div>
<h2 class="abs about-title">ABOUT US</h2>
<p class="abs about-copy">Nam libero tempore, cum soluta nobis est eligendi optio cumque nihil impedit quo minus id quod maxime placeat facere possimus, omnis voluptas as sumenda est, omnis dolor repellendus. Tempori bus autem quibusdam et aut officiis debitis aut rerum necessitati bus saepe eveniet ut et voluptates repudiandae...</p>
<div class="abs btn" style="left:110px;top:1871px;width:164px;height:45px">Read more <span class="dot"><svg width="7" height="8" viewBox="0 0 7 8"><path d="M2 1l3 3-3 3" stroke="#f05a1a" stroke-width="1.8" fill="none"/></svg></span></div>
<div class="abs about-photo" role="img" aria-label="Businessman shaking hands with a construction worker in hard hat"></div>

<div class="abs ghost" style="top:2080px">OUR PROJECTS</div>
<h2 class="abs heading" style="top:2100px;font-size:40px">OUR PROJECTS</h2>
<p class="abs lede" style="left:300px;width:600px;top:2172px">Lorem ipsum dolor sit amet, consectetur adipiscing elit, sed do eiusmod tempor incididunt ut exercitation ullamco laboris nisi ut labore et dolore magna aliqua.</p>
<div class="abs project" style="left:110px;background:linear-gradient(160deg,#c9c2ae,#7d7a52)" role="img" aria-label="Worker beside a cement mixer"></div>
<div class="abs project" style="left:358px;background:linear-gradient(160deg,#d8d4cc,#8a3a3a)" role="img" aria-label="Worker clearing debris indoors"></div>
<div class="abs project" style="left:608px;background:linear-gradient(160deg,#b49a6c,#5b4a35)" role="img" aria-label="Team reviewing plans under a timber frame"></div>
<div class="abs project" style="left:855px;background:linear-gradient(160deg,#c7ccd3,#6e4a38)" role="img" aria-label="Roofers working on a tiled roof"></div>
<div class="abs dots"><span></span><span></span><span class="on"></span><span></span></div>

<div class="abs quote-band"></div>
<svg class="abs band-arrow" style="left:42px" width="12" height="18" viewBox="0 0 12 18"><path d="M10 1 2 9l8 8" stroke="#fff" stroke-width="2.5" fill="none"/></svg>
<svg class="abs band-arrow" style="left:1142px" width="12" height="18" viewBox="0 0 12 18"><path d="M2 1l8 8-8 8" stroke="#fff" stroke-width="2.5" fill="none"/></svg>
<p class="abs quote-text">" At vero eos et accusamus et iusto odio dignissimos ducimus qui blanditiis praesentium voluptatum deleniti atque corrupti quos dolores et quas molestias excepturi sint occaecati cupiditate non provident, similique sunt in culpa qui officia deserunt mollitia animi, id est laborum et dolorum fuga. "</p>
<div class="abs quote-name">RENA OKAFOR, <small>Creative Manager</small></div>
<div class="abs quote-badge"><svg width="40" height="34" viewBox="0 0 40 34"><path fill="#fff" d="M0 34V18C0 8 5 2 15 0v6c-5 2-7 5-7 10h7v18zM22 34V18C22 8 27 2 37 0v6c-5 2-7 5-7 10h7v18z"/></svg></div>
<div class="abs quote-photo" role="img" aria-label="Portrait of the reviewer wearing a hard hat"></div>

<div class="abs ghost" style="top:2962px">LATEST BLOG POST</div>
<h2 class="abs heading" style="top:2982px;font-size:40px">LATEST BLOG POST</h2>
<p class="abs lede" style="left:300px;width:600px;top:3053px">Lorem ipsum dolor sit amet, consectetur adipiscing elit, sed do eiusmod tempor incididunt ut exercitation ullamco laboris nisi ut labore et dolore magna aliqua.</p>

<article class="abs post" style="left:110px">
  <div class="thumb" style="background:linear-gradient(160deg,#c8c2b3,#c89a1e)" role="img" aria-label="Worker in yellow overalls kneeling on site"></div>
  <div class="body">
    <h4>IPSAM VOLUPTATEM</h4>
    <div class="date"><svg width="11" height="11" viewBox="0 0 12 12"><path fill="#0d0b5e" d="M0 2h12v10H0zM2 0h2v3H2zM8 0h2v3H8z"/><path fill="#fff" d="M1 5h10v6H1z"/></svg>JAN 12, 2019</div>
    <p>At vero eos et accusam muset iusto odio dignissimos ducimus qui prae seum tre voluptatum...</p>
    <div class="meta"><span class="more">READ MORE <span style="width:12px;height:12px;border-radius:50%;background:#f05a1a;display:inline-block"></span></span><span>35 comments</span></div>
  </div>
</article>
<article class="abs post" style="left:616px">
  <div class="thumb" style="background:linear-gradient(160deg,#e0b84a,#5a4636)" role="img" aria-label="Two people talking on a construction site"></div>
  <div class="body">
    <h4>ACCUSAMUS ET IUSTO</h4>
    <div class="date"><svg width="11" height="11" viewBox="0 0 12 12"><path fill="#0d0b5e" d="M0 2h12v10H0zM2 0h2v3H2zM8 0h2v3H8z"/><path fill="#fff" d="M1 5h10v6H1z"/></svg>JAN 12, 2019</div>
    <p>At vero eos et accusam muset iusto odio dignissimos ducimus qui prae seum tre voluptatum...</p>
    <div class="meta"><span class="more">READ MORE <span style="width:12px;height:12px;border-radius:50%;background:#f05a1a;display:inline-block"></span></span><span>35 comments</span></div>
  </div>
</article>
<div class="abs btn" style="left:500px;top:3414px;width:200px;height:42px">View all blog <span class="dot"><svg width="7" height="8" viewBox="0 0 7 8"><path d="M2 1l3 3-3 3" stroke="#f05a1a" stroke-width="1.8" fill="none"/></svg></span></div>

<div class="abs foot-building" role="img" aria-label="Modern glass office building"></div>
<div class="abs foot-center"></div>
<div class="abs foot-map" role="img" aria-label="Street map with location pin"></div>
<div class="abs direction"><svg width="12" height="10" viewBox="0 0 12 10"><path d="M1 9V6a3 3 0 0 1 3-3h6M7 0l3 3-3 3" stroke="#1b1b1b" stroke-width="1.5" fill="none"/></svg>Get direction</div>
<div class="abs up-btn"><svg width="20" height="18" viewBox="0 0 20 18"><path d="M3 9l7-7 7 7M3 16l7-7 7 7" stroke="#0d0b5e" stroke-width="2.2" fill="none"/></svg></div>
<div class="abs foot-title" style="top:3636px">NEWSLETTER SUBSCRIPTION</div>
<div class="abs email-field">Email</div>
<div class="abs btn subscribe">Subscribe</div>
<div class="abs foot-title" style="top:3791px">CONTACT US</div>
<div class="abs foot-line" style="top:3825px"><svg width="13" height="13" viewBox="0 0 24 24"><path fill="#fff" d="M6.6 10.8a15 15 0 0 0 6.6 6.6l2.2-2.2a1 1 0 0 1 1-.25 11.4 11.4 0 0 0 3.6.6 1 1 0 0 1 1 1V20a1 1 0 0 1-1 1A17 17 0 0 1 3 4a1 1 0 0 1 1-1h3.5a1 1 0 0 1 1 1c0 1.25.2 2.45.6 3.6a1 1 0 0 1-.25 1z"/></svg>(+1) 555 010 2040</div>
<div class="abs foot-line" style="top:3853px"><svg width="13" height="10" viewBox="0 0 24 18"><path fill="#fff" d="M0 0h24v18H0zM2 2l10 7 10-7z"/></svg>info@marlotidyyard.com</div>
<div class="abs foot-line" style="top:3898px">© 2019 Marlo Tidy Yard. All Rights Reserved.</div>

</body>
</html>
```